Webdesign für Branchenverzeichnis
Zielgruppe
Wir-bauen-Brücken – das Branchenverzeichnis der Selbstverantwortlichen.
Der Anbieter präsentiert sich mit seinem Namen und der URL - ähnlich wie bei 'blaue Blätter' oder Torkwerk.
Aufgabenstellung
Das Branchenverzeichnis sollte neutral und gleichzeitig hochwertig sein. Die Hauptfarben sind Gold, Schwarz und Weiß. Logo und Corporate Design wurden bereits entwickelt

```html
<!DOCTYPE html>
<html lang="de">
<head>
<meta charset="utf-8">
<title>Wir-bauen-Brücken – Branchenverzeichnis</title>
<link href="https://fonts.googleapis.com/css2?family=Quicksand:wght@400;500;600;700&display=swap" rel="stylesheet">
<style>
:root{
  --gold:#d6b364;
  --gold-text:#d2a957;
  --card:#fbf3d6;
  --card-line:#eadba8;
  --ink:#1e1e1e;
  --dark:#3a3a3a;
  --muted:#666;
  --page:#fafafa;
  --white:#fff;
}
*{box-sizing:border-box;margin:0;padding:0}
html,body{width:1088px;height:1200px;overflow:hidden}
body{position:relative;background:var(--page);font-family:"Quicksand",sans-serif;color:var(--ink)}

.site-header{position:absolute;left:0;top:0;width:1088px;height:57px;background:linear-gradient(#5a5a5a,#3a3a3a)}
.brand{position:absolute;left:143px;top:13px;display:flex;align-items:center;gap:5px;color:var(--gold);font-size:7.5px;font-weight:600;line-height:9px}
.brand-dot{width:30px;height:30px;border:2px solid var(--gold);border-radius:50%;flex:none}
.brand-name{width:46px}
.nav a{position:absolute;top:23px;font-size:8.5px;font-weight:700;letter-spacing:1px;color:var(--white);text-decoration:none}
.nav a.active{color:var(--gold)}
.icon-box{position:absolute;top:17px;width:23px;height:23px;border:1px solid var(--gold);background:#4a4a4a;display:flex;align-items:center;justify-content:center}
.cta{position:absolute;left:833px;top:15px;width:113px;height:26px;background:var(--gold);color:var(--white);font-size:7.5px;font-weight:600;letter-spacing:.8px;display:flex;align-items:center;justify-content:center}

.hero-title{position:absolute;top:97px;width:1088px;text-align:center;font-size:21px;font-weight:700;letter-spacing:3.5px}
.hero-title span{color:var(--gold)}
.hero-sub{position:absolute;top:131px;width:1088px;text-align:center;font-size:9.5px;letter-spacing:1px;color:#333}

.search{position:absolute;left:150px;top:164px;width:805px;height:85px;background:var(--gold);box-shadow:0 3px 8px rgba(0,0,0,.15)}
.field{position:absolute;top:25px;width:170px;height:34px;background:var(--white);border:1px solid #e6d9b5;font-size:10px;color:#666;padding-left:12px;display:flex;align-items:center}
.field svg{position:absolute;right:10px;top:9px}
.search-btn{position:absolute;left:657px;top:25px;width:113px;height:34px;background:var(--dark);color:var(--white);font-size:7.5px;font-weight:700;letter-spacing:.8px;display:flex;align-items:center;justify-content:center}

.results-title{position:absolute;left:151px;top:269px;font-size:12.5px;color:#333}
.results-title span{color:var(--gold-text)}
.results-count{position:absolute;left:151px;top:288px;font-size:8.5px;color:var(--muted);letter-spacing:.3px}
.sort-label{position:absolute;left:473px;top:288px;font-size:8.5px;color:var(--muted)}
.sort-select{position:absolute;left:546px;top:284px;width:86px;height:19px;border:1px solid #ddd;background:var(--white);font-size:6.5px;color:#888;padding-left:8px;display:flex;align-items:center}
.sort-select svg{position:absolute;right:6px;top:6px}
.rule{position:absolute;left:151px;top:310px;width:481px;height:1px;background:#ccc}

.card{position:absolute;left:151px;width:481px;height:68px;background:var(--card);border:1px solid var(--card-line);box-shadow:0 2px 4px rgba(0,0,0,.08)}
.card-logo{position:absolute;left:18px;top:11px;width:46px;text-align:center;color:var(--gold);font-size:5.5px;font-weight:600}
.card-logo .dot{width:30px;height:30px;border:2px solid var(--gold);border-radius:50%;margin:0 auto 4px}
.card-name{position:absolute;left:102px;top:16px;font-size:13px;font-weight:500;letter-spacing:.8px}
.card-meta{position:absolute;left:102px;top:38px;font-size:7px;color:#444;display:flex;gap:26px;letter-spacing:.3px}
.card-meta span{display:flex;align-items:center;gap:4px}
.card-btn{position:absolute;left:392px;top:22px;width:71px;height:23px;border:1px solid var(--dark);font-size:6.5px;letter-spacing:.6px;color:#444;display:flex;align-items:center;justify-content:center}
.card-btn.filled{background:var(--dark);color:var(--white)}

.map{position:absolute;left:677px;top:352px;width:278px;height:560px;background:linear-gradient(160deg,#efe9d9 0%,#e6e0cf 45%,#cfe3e6 70%,#a9d3dd 100%)}

.pager{position:absolute;top:952px;left:309px;display:flex;gap:6px}
.pager div{width:28px;height:28px;border:1px solid var(--gold);display:flex;align-items:center;justify-content:center;font-size:11px;color:#444}
.pager div.current{color:var(--gold);font-weight:700}

.site-footer{position:absolute;left:0;top:1027px;width:1088px;height:173px;background:linear-gradient(#5a5a5a,#262626);color:var(--white)}
.foot-brand{position:absolute;left:240px;top:40px;width:60px;text-align:center;font-size:7px;font-weight:600}
.foot-brand .dot{width:52px;height:52px;border:2px solid var(--white);border-radius:50%;margin:0 auto 4px}
.foot-col{position:absolute;top:42px}
.foot-col h3{font-size:10px;font-weight:700;letter-spacing:.5px;margin-bottom:10px}
.foot-col p{font-size:8.5px;line-height:14px;width:160px}
.foot-col a{display:block;color:var(--white);font-size:8.5px;text-decoration:none;line-height:19px}
.foot-col a.u{text-decoration:underline;margin-top:10px}
</style>
</head>
<body>

<header class="site-header">
  <div class="brand"><div class="brand-dot"></div><div class="brand-name">Wir-bauen-<br>Brücken</div></div>
  <nav class="nav">
    <a style="left:261px">HOME</a>
    <a class="active" style="left:328px">SUCHEN</a>
    <a style="left:408px">ÜBER UNS</a>
    <a style="left:493px">MITGLIEDSCHAFT</a>
    <a style="left:612px">KONTAKT</a>
  </nav>
  <div class="icon-box" style="left:747px">
    <svg width="15" height="10"><rect width="15" height="3.4" fill="#000"/><rect y="3.3" width="15" height="3.4" fill="#d00"/><rect y="6.6" width="15" height="3.4" fill="#fc0"/></svg>
  </div>
  <div class="icon-box" style="left:777px">
    <svg width="12" height="12"><circle cx="6" cy="4" r="3" fill="#d6b364"/><path d="M0 12c0-4 3-5 6-5s6 1 6 5z" fill="#d6b364"/></svg>
  </div>
  <div class="cta">MITGLIED WERDEN</div>
</header>

<h1 class="hero-title">WIR ZEIGEN <span>UNTERNEHMER</span></h1>
<p class="hero-sub">Suche in deiner Region und finde neue Unternehmen in vielen Branchen &amp; Ländern.</p>

<section class="search">
  <div class="field" style="left:34px">Unternehmen, Name
    <svg width="16" height="15"><path d="M8 1L1 8h2v6h4v-4h2v4h4V8h2z" fill="#d6b364"/></svg></div>
  <div class="field" style="left:233px">Stadt, PLZ oder Land
    <svg width="16" height="16"><circle cx="8" cy="8" r="6" fill="none" stroke="#d6b364" stroke-width="1.5"/><circle cx="8" cy="8" r="3" fill="#d6b364"/></svg></div>
  <div class="field" style="left:431px">Branche
    <svg width="14" height="14"><path d="M2 5l5 5 5-5" fill="none" stroke="#d6b364" stroke-width="1.6"/></svg></div>
  <div class="search-btn">SUCHEN</div>
</section>

<div class="results-title">Ihre Suchergebnisse für: <span>IT &amp; Marketing</span></div>
<div class="results-count">Zeige 7 von 25 Brancheneinträgen</div>
<div class="sort-label">Sortieren nach</div>
<div class="sort-select">Firmenname A-Z
  <svg width="8" height="6"><path d="M1 1l3 3 3-3" fill="none" stroke="#aaa" stroke-width="1"/></svg></div>
<div class="rule"></div>

<article class="card" style="top:352px">
  <div class="card-logo"><div class="dot"></div>Wir-bauen-Brücken</div>
  <div class="card-name">Firmenname Jens Falk Consulting</div>
  <div class="card-meta"><span><svg width="7" height="7"><rect x=".5" y="1" width="6" height="5.5" fill="none" stroke="#d6b364"/></svg>IT &amp; Marketing</span><span><svg width="6" height="8"><path d="M3 0a3 3 0 0 1 3 3c0 2-3 5-3 5S0 5 0 3a3 3 0 0 1 3-3z" fill="#d6b364"/></svg>München</span></div>
  <div class="card-btn filled">ZUR WEBSITE</div>
</article>
<article class="card" style="top:434px">
  <div class="card-logo"><div class="dot"></div>Wir-bauen-Brücken</div>
  <div class="card-name">Firmenname Jens Falk Consulting</div>
  <div class="card-meta"><span><svg width="7" height="7"><rect x=".5" y="1" width="6" height="5.5" fill="none" stroke="#d6b364"/></svg>IT &amp; Marketing</span><span><svg width="6" height="8"><path d="M3 0a3 3 0 0 1 3 3c0 2-3 5-3 5S0 5 0 3a3 3 0 0 1 3-3z" fill="#d6b364"/></svg>München</span></div>
  <div class="card-btn">ZUR WEBSITE</div>
</article>
<article class="card" style="top:516px">
  <div class="card-logo"><div class="dot"></div>Wir-bauen-Brücken</div>
  <div class="card-name">Firmenname Jens Falk Consulting</div>
  <div class="card-meta"><span><svg width="7" height="7"><rect x=".5" y="1" width="6" height="5.5" fill="none" stroke="#d6b364"/></svg>IT &amp; Marketing</span><span><svg width="6" height="8"><path d="M3 0a3 3 0 0 1 3 3c0 2-3 5-3 5S0 5 0 3a3 3 0 0 1 3-3z" fill="#d6b364"/></svg>München</span></div>
  <div class="card-btn">ZUR WEBSITE</div>
</article>
<article class="card" style="top:598px">
  <div class="card-logo"><div class="dot"></div>Wir-bauen-Brücken</div>
  <div class="card-name">Firmenname Jens Falk Consulting</div>
  <div class="card-meta"><span><svg width="7" height="7"><rect x=".5" y="1" width="6" height="5.5" fill="none" stroke="#d6b364"/></svg>IT &amp; Marketing</span><span><svg width="6" height="8"><path d="M3 0a3 3 0 0 1 3 3c0 2-3 5-3 5S0 5 0 3a3 3 0 0 1 3-3z" fill="#d6b364"/></svg>München</span></div>
  <div class="card-btn">ZUR WEBSITE</div>
</article>
<article class="card" style="top:680px">
  <div class="card-logo"><div class="dot"></div>Wir-bauen-Brücken</div>
  <div class="card-name">Firmenname Jens Falk Consulting</div>
  <div class="card-meta"><span><svg width="7" height="7"><rect x=".5" y="1" width="6" height="5.5" fill="none" stroke="#d6b364"/></svg>IT &amp; Marketing</span><span><svg width="6" height="8"><path d="M3 0a3 3 0 0 1 3 3c0 2-3 5-3 5S0 5 0 3a3 3 0 0 1 3-3z" fill="#d6b364"/></svg>München</span></div>
  <div class="card-btn">ZUR WEBSITE</div>
</article>
<article class="card" style="top:762px">
  <div class="card-logo"><div class="dot"></div>Wir-bauen-Brücken</div>
  <div class="card-name">Firmenname Jens Falk Consulting</div>
  <div class="card-meta"><span><svg width="7" height="7"><rect x=".5" y="1" width="6" height="5.5" fill="none" stroke="#d6b364"/></svg>IT &amp; Marketing</span><span><svg width="6" height="8"><path d="M3 0a3 3 0 0 1 3 3c0 2-3 5-3 5S0 5 0 3a3 3 0 0 1 3-3z" fill="#d6b364"/></svg>München</span></div>
  <div class="card-btn">ZUR WEBSITE</div>
</article>
<article class="card" style="top:844px">
  <div class="card-logo"><div class="dot"></div>Wir-bauen-Brücken</div>
  <div class="card-name">Firmenname Jens Falk Consulting</div>
  <div class="card-meta"><span><svg width="7" height="7"><rect x=".5" y="1" width="6" height="5.5" fill="none" stroke="#d6b364"/></svg>IT &amp; Marketing</span><span><svg width="6" height="8"><path d="M3 0a3 3 0 0 1 3 3c0 2-3 5-3 5S0 5 0 3a3 3 0 0 1 3-3z" fill="#d6b364"/></svg>München</span></div>
  <div class="card-btn">ZUR WEBSITE</div>
</article>

<div class="map" role="img" aria-label="Stadtkarte mit Standortmarkierungen der Suchergebnisse"></div>

<nav class="pager">
  <div class="current">1</div><div>2</div><div>3</div><div>4</div><div>5</div>
</nav>

<footer class="site-footer">
  <div class="foot-brand"><div class="dot"></div>Wir-bauen-Brücken</div>
  <div class="foot-col" style="left:325px">
    <h3>WIR BAUEN BRÜCKEN</h3>
    <p>Duis sed odio sit amet nibh vulputate cursus a sit amet mauris Morbi accu.</p>
    <a class="u">Über uns</a>
  </div>
  <div class="foot-col" style="left:587px">
    <h3>WEBSITE</h3>
    <a>Unternehmen suchen</a><a>Mitgliedschaft</a><a>Kontakt</a>
  </div>
  <div class="foot-col" style="left:760px">
    <h3>RECHTLICHES</h3>
    <a>Impressum</a><a>Datenschutz</a><a>AGB</a>
  </div>
</footer>

</body>
</html>
```